Real estate Investment post card Design

I need a post card for Real Estate Marketing.

There are several similar cards on line.
Please see the post cards in this link to clipvora
https://www.clipvora.com/watch?v=pTw8Lm3Qz-Y7
At 1:18 the back of the card is very good.
For front of the card please refer to attached example gif.

Please also check the examples posted by me.

Everything needs to be the same except
1. Teo Gets Homes
2. Phone number 274 859 4167
3. Website www.brookdwellguide.com
4. Email info@brookdwellguide.com
5. Picture needs to be replaced with my picture

The postcards need to be 2 sides and in color

Please let me know

Target Market(s)

Home owners who want to sell their houses for quick settlement and cash

Industry/Entity Type

Real Estate

Requirements
Must have
• I am copying this from another project as i think these instructions are valid for this project as well.
• Attention Designers - Special Requirements
• This project has special US Postcard Design requirements that apply to all submissions. The project is part of a print initiative, meaning that the selected design will be sent directly to print. If you have not, click download the templates below and ensure your design follows them before submitting.
• I plan to print the Post card by printolana in their Jumbo Format... copied below
• Document Trim Size
• 8.52" x 5.47"
• 216 x 139 mm
• 2556 x 1642 pixels
• Full Bleed Size
• Horizontal
• 8.64" x 5.59"
• 219 x 142 mm
• 2592 x 1677 pixels
• NOTE Please make sure you put return address on the post card
• 4837 8TH ST., PO Box. 5926
• NEW HYDE PARK, NY 11040
Nice to have
• Please see if you can add pictures that signify cash $$ and houses in the project. See the attached clipvora.
Should not have
• Too much text on the first page

```html
<!DOCTYPE html>
<html lang="en">
<head>
<meta charset="utf-8">
<title>Teo Gets Homes – Postcard</title>
<link href="https://fonts.googleapis.com/css2?family=Oswald:wght@500;600&family=Roboto+Condensed:wght@700&family=Lato:wght@400;700&display=swap" rel="stylesheet">
<style>
  :root {
    --blue: #1e6fa6;
    --blue-light: #4a86c8;
    --yellow: #f0c419;
    --ink: #2b2b2d;
    --black: #111;
    --paper: #ffffff;
    --stage: #e9e6e1;
    --stamp: #cfcfcf;
  }
  * { box-sizing: border-box; margin: 0; padding: 0; }
  html, body { width: 907px; height: 1200px; overflow: hidden; }
  body { background: var(--stage); position: relative; font-family: "Lato", sans-serif; }

  .card {
    position: absolute; left: 118px; width: 674px; height: 436px;
    background: var(--paper); overflow: hidden;
    box-shadow: 0 4px 14px rgba(0,0,0,.25);
  }
  .card--front { top: 138px; }
  .card--back { top: 638px; }
  .card svg.waves { position: absolute; inset: 0; width: 674px; height: 436px; }

  /* front */
  .hero-image {
    position: absolute; left: 12px; top: 78px; width: 330px; height: 220px;
    background: radial-gradient(ellipse at 40% 40%, #c0392b 0 18%, #a8866a 32%, #8fa07f 55%, #e8ebe6 75%, transparent 78%);
  }
  .front-title {
    position: absolute; right: 14px; top: 20px;
    font-family: "Roboto Condensed", sans-serif; font-weight: 700;
    font-size: 38px; color: var(--blue); letter-spacing: .3px;
  }
  .cash-band {
    position: absolute; left: 352px; right: 0; top: 74px; height: 66px;
    background: linear-gradient(90deg, rgba(240,196,25,0) 0%, var(--yellow) 75%);
  }
  .cash-band span {
    position: absolute; right: 18px; top: 0;
    font-family: "Oswald", sans-serif; font-weight: 600; font-size: 54px; line-height: 66px; color: var(--black);
  }
  .front-sub {
    position: absolute; right: 12px; top: 150px;
    font-family: "Roboto Condensed", sans-serif; font-weight: 700; font-size: 22px; color: var(--black);
  }
  .call-band {
    position: absolute; left: 352px; right: 0; top: 187px; height: 66px;
    background: linear-gradient(90deg, rgba(30,111,166,0) 0%, #9ab6d0 35%, var(--blue) 100%);
  }
  .call-band span {
    position: absolute; right: 14px; top: 3px; text-align: left;
    font-family: "Roboto Condensed", sans-serif; font-weight: 700; font-size: 24px; line-height: 30px; color: var(--black);
  }
  .front-phone {
    position: absolute; right: 20px; top: 266px;
    font-family: "Roboto Condensed", sans-serif; font-weight: 700; font-size: 25px; color: var(--blue);
  }

  .contact { position: absolute; list-style: none; font-family: "Lato", sans-serif; font-weight: 700; font-size: 13px; color: #fff; }
  .contact li { display: flex; align-items: center; gap: 6px; height: 16px; }
  .contact svg { width: 9px; height: 9px; fill: var(--yellow); }
  .card--front .contact { left: 38px; top: 354px; }
  .card--back .contact { left: 28px; top: 339px; }
  .card--back .contact li:first-child { color: var(--yellow); }

  /* back */
  .back-title {
    position: absolute; left: 25px; top: 44px;
    font-family: "Roboto Condensed", sans-serif; font-weight: 700; font-size: 28px; color: var(--blue);
  }
  .back-copy {
    position: absolute; left: 25px; top: 84px; width: 246px;
    font-size: 9.6px; line-height: 11.8px; color: #222; text-align: justify;
  }
  .portrait {
    position: absolute; left: 199px; top: 200px; width: 162px; height: 162px; border-radius: 50%;
    border: 5px solid var(--blue); box-shadow: inset 0 0 0 4px #fff;
    background: linear-gradient(180deg, #d9d9d9 0%, #8a8a8a 60%, #2d2d2d 100%);
  }
  .stamp { position: absolute; right: 12px; top: 12px; width: 59px; height: 68px; background: var(--stamp); }
</style>
</head>
<body>

<section class="card card--front">
  <svg class="waves" viewBox="0 0 674 436" aria-hidden="true">
    <path d="M100,316 C260,286 400,302 500,370 C560,410 630,382 674,336 L674,436 L0,436 Z" fill="var(--yellow)"/>
    <path d="M220,303 C330,290 420,300 500,336 C570,366 630,346 674,298 L674,330 C630,378 560,398 498,366 C420,322 330,302 220,303 Z" fill="var(--blue)"/>
    <path d="M0,336 C140,300 300,292 436,436 L0,436 Z" fill="#fff"/>
    <path d="M0,342 C140,308 296,300 426,436 L0,436 Z" fill="var(--ink)"/>
  </svg>
  <div class="hero-image" role="img" aria-label="Model house with red roof on a stack of dollar bills with house keys"></div>
  <h1 class="front-title">TEO GETS HOMES</h1>
  <div class="cash-band"><span>CA$H!</span></div>
  <p class="front-sub">Any condition Any situation</p>
  <div class="call-band"><span>Call today for a free<br>private consultation</span></div>
  <p class="front-phone">274 859 4167</p>
  <ul class="contact">
    <li><svg viewBox="0 0 10 10"><path d="M2,0 L4,2 L3,3.5 Q4.5,6 6.5,7 L8,6 L10,8 L8.5,10 Q1,8 0,1.5 Z"/></svg>274 859 4167</li>
    <li><svg viewBox="0 0 10 10"><path d="M0,2 H10 V8 H0 Z"/></svg>www.brookdwellguide.com</li>
    <li><svg viewBox="0 0 10 10"><circle cx="5" cy="5" r="5"/></svg>info@brookdwellguide.com</li>
  </ul>
</section>

<section class="card card--back">
  <svg class="waves" viewBox="0 0 674 436" aria-hidden="true">
    <circle cx="120" cy="230" r="302" fill="var(--ink)"/>
    <circle cx="120" cy="230" r="288" fill="#fff"/>
    <circle cx="120" cy="230" r="283" fill="var(--blue-light)"/>
    <circle cx="120" cy="230" r="274" fill="#fff"/>
    <circle cx="120" cy="230" r="270" fill="var(--yellow)"/>
    <circle cx="120" cy="230" r="244" fill="#fff"/>
    <path d="M0,268 C80,252 180,250 290,286 L290,300 C180,268 80,270 0,282 Z" fill="var(--yellow)"/>
    <path d="M0,256 C90,238 190,240 300,270 L296,282 C190,254 90,252 0,266 Z" fill="var(--blue-light)"/>
    <path d="M0,292 C90,276 190,276 300,304 L300,436 L0,436 Z" fill="var(--ink)"/>
  </svg>
  <div class="stamp"></div>
  <h2 class="back-title">TEO GETS HOMES</h2>
  <p class="back-copy">Lorem Ipsum is simply dummy text of the printing and typesetting industry. Lorem Ipsum has been the industry's standard dummy text ever since the 1500s, when an unknown printer took a galley of type and scrambled it to make a type specimen book. It has survived not only five centuries, but also the leap into electronic typesetting, remaining essentially unchanged. It was popularised in the 1960s with the release of Typorail sheets containing Lorem Ipsum passages, and more recently with desktop publishing software like Folio Layoutdesk including versions of Lorem Ipsum</p>
  <div class="portrait" role="img" aria-label="Black and white portrait photo of the agent in a suit"></div>
  <ul class="contact">
    <li><svg viewBox="0 0 10 10"><path d="M2,0 L4,2 L3,3.5 Q4.5,6 6.5,7 L8,6 L10,8 L8.5,10 Q1,8 0,1.5 Z"/></svg>274 859 4167</li>
    <li><svg viewBox="0 0 10 10"><path d="M0,2 H10 V8 H0 Z"/></svg>www.brookdwellguide.com</li>
    <li><svg viewBox="0 0 10 10"><circle cx="5" cy="5" r="5"/></svg>info@brookdwellguide.com</li>
  </ul>
</section>

</body>
</html>
```